Flyer-Design für Bio Gemüsebau
Sehr gut und schnell auf unsere Bedürfnisse und konkreten Änderungswünsche eingegangen.
Zielgruppe
Bio-Gemüseanbau: Bei uns gibt es über 45 Gemüsekulturen von Aubergine bis Zwiebeln.
Endverbraucher, Menschen, die sich gerne gesund ernähren und Wert auf Nachhaltigkeit und Regionalität legen.
Wir verkaufen am Straßenstand sowie an Abonnenten.
Wir heißen 'Gemüsehof Kleiner Acker' und haben bereits ein Logo (siehe Anhang)
Aufgabenstellung
Es wäre prima, wenn der Flyer allgemeine Infos (siehe Worddatei) zu dem Gemüseangebot und der Gärtnerei enthält.
Wir werden zudem einige Fotos zur Auswahl beilegen.
Es wäre ganz toll, wenn an prominenter Stelle ein Foto Platz finden würde, an dessen Stelle man bei Bedarf z.B. auf eine Veranstaltung oder eine bestimmte Aktion hinweisen könnte. Also, dass wir bei Bedarf dieses Foto entfernen und diesen Platz für einen aktuellen Hinweis nutzen könnten.
Ansonsten sind wir offen, was das Format des Flyers angeht. Wenn das Design auf einem ökologischen Papier funktionieren könnte, wäre das super, da wir ja ein Biobetrieb sind.
Unser Logo muss auf jeden Fall mit drauf, das ist inzwischen schon etabliert.
Weitere Infos auf unserer Homepage www.gemuesehof-kleineracker-beispiel.de (unter Galerie sind auch weitere Fotos, die verwendet werden könnten)
Vielen Dank.

```html
<!DOCTYPE html>
<html lang="de">
<head>
<meta charset="utf-8">
<title>Flyer Gemüsehof Kleiner Acker</title>
<link rel="stylesheet" href="https://fonts.googleapis.com/css2?family=Oswald:wght@300;400;500;600&family=Permanent+Marker&display=swap">
<style>
  :root {
    --green: #9de491;
    --green-mid: #b6ebab;
    --green-light: #d6f5d0;
    --green-pale: #ecfae9;
    --yellow: #fed716;
    --teal: #046b5c;
    --ink: #111111;
    --text: #222222;
    --bullet: #3e4b49;
    --stage: #e4e5e7;
    --body-font: "Oswald", sans-serif;
    --brush-font: "Permanent Marker", cursive;
  }
  * { box-sizing: border-box; margin: 0; padding: 0; }
  html, body { width: 1200px; height: 859px; overflow: hidden; }
  body { background: var(--stage); position: relative; font-family: var(--body-font); color: var(--text); }

  .flyer { position: absolute; width: 475px; height: 647px; overflow: hidden; box-shadow: 0 2px 10px rgba(0,0,0,.15); }
  .flyer--front { left: 98px; top: 96px; background: var(--green); }
  .flyer--back { left: 640px; top: 96px; background: #ffffff; }
  .rings { position: absolute; inset: 0; }
  .abs { position: absolute; }

  .brand { position: absolute; display: flex; align-items: center; gap: 6px; }
  .brand__dot { border-radius: 50%; background: var(--teal); flex: none; }
  .brand__name { font-family: var(--body-font); font-weight: 500; color: var(--ink); white-space: nowrap; }
  .flyer--front .brand { left: 140px; top: 40px; }
  .flyer--front .brand__dot { width: 26px; height: 26px; }
  .flyer--front .brand__name { font-size: 21px; }
  .flyer--back .brand { left: 300px; top: 32px; }
  .flyer--back .brand__dot { width: 14px; height: 14px; }
  .flyer--back .brand__name { font-size: 12px; }

  .front-title { left: 0; right: 0; top: 100px; text-align: center; font-family: var(--brush-font); font-size: 37px; color: var(--ink); transform: rotate(-1deg); }
  .front-intro { left: 40px; right: 40px; top: 156px; text-align: center; font-weight: 300; font-size: 15px; line-height: 21px; color: var(--ink); }
  .front-hours { left: 10px; right: 10px; top: 214px; text-align: center; font-weight: 500; font-size: 15px; line-height: 21px; color: var(--ink); }
  .front-text { left: 34px; top: 264px; font-weight: 300; font-size: 14.5px; line-height: 19.7px; color: var(--ink); white-space: nowrap; }

  .feature { position: absolute; }
  .feature__shadow { position: absolute; border-radius: 50%; background: linear-gradient(135deg, rgba(80,110,80,0) 30%, rgba(70,100,70,.55)); }
  .feature__ring { position: absolute; border-radius: 50%; background: var(--yellow); }
  .feature__photo { position: absolute; border-radius: 50%; overflow: hidden; }
  .event-label { position: absolute; left: 0; right: 0; text-align: center; font-family: var(--brush-font); color: #ffffff; text-shadow: 0 1px 3px rgba(0,0,0,.5); white-space: nowrap; }

  .basket-photo { position: absolute; left: 0; top: 418px; width: 304px; height: 184px; border-radius: 0 120px 0 0; background: radial-gradient(ellipse at 55% 45%, #6fae4a 0%, #c9b23a 38%, #b6483a 55%, #5a4a38 78%, rgba(90,74,56,.9) 100%); }

  .footer { position: absolute; left: 0; right: 0; bottom: 0; background: var(--yellow); }
  .flyer--front .footer { height: 47px; }
  .flyer--back .footer { height: 81px; }
  .footer__item { position: absolute; text-align: center; color: var(--ink); font-weight: 300; white-space: nowrap; transform: translateX(-50%); }
  .footer__rule { position: absolute; width: 1px; background: var(--ink); }
  .flyer--front .footer__item { font-size: 6.4px; line-height: 10px; }
  .flyer--back .footer__item { font-size: 9.4px; line-height: 13px; }
  .icon { display: block; margin: 0 auto; }

  .back-title { left: 38px; top: 34px; font-family: var(--brush-font); font-size: 21px; line-height: 27px; color: var(--ink); transform: rotate(-1.5deg); transform-origin: left top; white-space: nowrap; }
  .box-item { position: absolute; font-weight: 500; color: var(--ink); white-space: nowrap; line-height: 20px; }
  .box-item--lg { font-size: 17px; }
  .box-item--md { font-size: 15px; }
  .back-text { left: 51px; top: 343px; font-weight: 300; font-size: 13.5px; line-height: 19.7px; color: var(--ink); }
  .back-text__line { display: block; white-space: nowrap; text-align: justify; text-align-last: justify; }
  .back-text__line--end { text-align: left; text-align-last: left; }
  .short-title { left: 280px; top: 342px; font-family: var(--brush-font); font-size: 15px; line-height: 20px; color: var(--ink); transform: rotate(-2deg); white-space: nowrap; }
  .fact { position: absolute; font-weight: 300; font-size: 15px; line-height: 21px; color: var(--bullet); white-space: nowrap; }
</style>
</head>
<body>

<!-- Front side -->
<section class="flyer flyer--front">
  <svg class="rings" width="475" height="647" viewBox="0 0 475 647" aria-hidden="true">
    <circle cx="20" cy="20" r="180" fill="var(--green)"/>
    <circle cx="20" cy="20" r="150" fill="#a9e79e"/>
    <circle cx="20" cy="20" r="115" fill="var(--green-mid)"/>
    <circle cx="20" cy="20" r="80" fill="var(--green-light)"/>
    <circle cx="20" cy="20" r="50" fill="var(--green-pale)"/>
    <circle cx="20" cy="20" r="28" fill="#ffffff"/>
    <circle cx="140" cy="520" r="170" fill="#a9e79e"/>
    <circle cx="140" cy="520" r="130" fill="var(--green-mid)"/>
    <circle cx="140" cy="520" r="95" fill="var(--green-light)"/>
    <circle cx="140" cy="520" r="60" fill="#ffffff"/>
  </svg>

  <div class="brand"><span class="brand__dot"></span><span class="brand__name">Gemüsehof Kleiner Acker</span></div>

  <h1 class="abs front-title">Bio Gemüseanbau</h1>
  <p class="abs front-intro">Wir sind eine kleine Vielfaltsgärtnerei in Musterdorf, die Gemüse im Einklang mit der Natur produziert.</p>
  <p class="abs front-hours">Unsere frischen Produkte gibt’s an unserem Straßenstand direkt am feld.<br>Öffnungszeiten : Sa 10-12 / Fr 10-14</p>
  <p class="abs front-text">Wenn Du mehr wissen willst über unseren Anbau<br>(Market Gardening) und unser Gemüsesorti-<br>ment von A bis Z, besuche unsere<br>Internetseite.<br>Für eine ganze Saison kann man aber<br>auch eine Gemüsekiste bei uns abonnie-<br>ren.</p>

  <div class="basket-photo" role="img" aria-label="Foto: Korb mit frischem Gemüse – Rote Bete, Paprika, Salat und Tomaten"></div>

  <div class="feature" style="left:231px; top:253px;">
    <div class="feature__shadow" style="left:12px; top:14px; width:228px; height:228px;"></div>
    <div class="feature__ring" style="left:0; top:0; width:228px; height:228px;"></div>
    <div class="feature__photo" style="left:19px; top:19px; width:190px; height:190px; background: linear-gradient(180deg, #4d6a3e 0%, #7b8a6a 30%, #9aa08e 45%, #7a7a5e 60%, #8b7f66 100%);" role="img" aria-label="Luftbild der Gärtnerei mit Folientunneln und Beeten – Platz für aktuellen Hinweis">
      <span class="event-label" style="top:82px; font-size:21px;">Your event here</span>
    </div>
  </div>

  <footer class="footer">
    <div class="footer__item" style="left:193px; top:9px;">
      <svg class="icon" width="18" height="18" viewBox="0 0 24 24" aria-hidden="true"><circle cx="12" cy="12" r="12" fill="var(--teal)"/><circle cx="12" cy="9.5" r="3.6" fill="var(--yellow)"/><path d="M5.5 18c1.2-3 3.7-4.3 6.5-4.3s5.3 1.3 6.5 4.3z" fill="var(--yellow)"/></svg>
      <span>Jonas Berger (0152 1234 5678)</span>
    </div>
    <span class="footer__rule" style="left:251px; top:8px; height:31px;"></span>
    <div class="footer__item" style="left:308px; top:9px;">
      <svg class="icon" width="18" height="18" viewBox="0 0 24 24" aria-hidden="true"><circle cx="12" cy="12" r="12" fill="var(--teal)"/><rect x="6" y="8" width="12" height="8.5" rx="1" fill="var(--yellow)"/><path d="M6.5 8.5l5.5 4.5 5.5-4.5" fill="none" stroke="var(--teal)" stroke-width="1.2"/></svg>
      <span>Feldweg 7, 12345 Musterdorf</span>
    </div>
    <span class="footer__rule" style="left:366px; top:8px; height:31px;"></span>
    <div class="footer__item" style="left:423px; top:14px;">www.gemuesehof-kleineracker-beispiel.de<br>info@gemuesehof-kleineracker-beispiel.de</div>
  </footer>
</section>

<!-- Back side -->
<section class="flyer flyer--back">
  <svg class="rings" width="475" height="647" viewBox="0 0 475 647" aria-hidden="true">
    <defs><linearGradient id="fadeBottom" x1="0" y1="0" x2="0" y2="1"><stop offset="0" stop-color="#ffffff" stop-opacity="0"/><stop offset="1" stop-color="#c8c8cc"/></linearGradient></defs>
    <circle cx="450" cy="80" r="330" fill="var(--green-pale)"/>
    <circle cx="450" cy="80" r="270" fill="var(--green-light)"/>
    <circle cx="450" cy="80" r="205" fill="#c4efbb"/>
    <circle cx="450" cy="80" r="145" fill="var(--green-mid)"/>
    <circle cx="450" cy="80" r="90" fill="var(--green)"/>
    <circle cx="30" cy="600" r="140" fill="var(--green-pale)"/>
    <circle cx="30" cy="600" r="105" fill="var(--green-light)"/>
    <circle cx="30" cy="600" r="72" fill="#c4efbb"/>
    <circle cx="30" cy="600" r="40" fill="var(--green-mid)"/>
    <rect x="0" y="540" width="475" height="30" fill="url(#fadeBottom)"/>
    <line x1="371" y1="127" x2="202" y2="542" stroke="#7fd66f" stroke-width="1"/>
  </svg>

  <div class="brand"><span class="brand__dot"></span><span class="brand__name">Gemüsehof Kleiner Acker</span></div>

  <h2 class="abs back-title">Inhalt der Abo-Kiste<br>(Beispiel aus der<br>Saison 2021)</h2>

  <div class="feature" style="left:22px; top:117px;">
    <div class="feature__shadow" style="left:5px; top:14px; width:200px; height:200px;"></div>
    <div class="feature__ring" style="left:0; top:0; width:200px; height:200px;"></div>
    <div class="feature__photo" style="left:16px; top:16px; width:168px; height:168px; background: radial-gradient(circle at 50% 50%, #a5b36a 0%, #6f9a4a 40%, #8a4d5a 70%, #5f7a52 100%);" role="img" aria-label="Foto: Inhalt einer Gemüsekiste – Salat, Tomaten, Möhren, Aubergine, Gurke und Kohlrabi"></div>
  </div>

  <span class="box-item box-item--lg" style="left:240px; top:117px;">Woche 33 (August)</span>
  <span class="box-item box-item--lg" style="left:275px; top:141px;">1 Aubergine</span>
  <span class="box-item box-item--lg" style="left:251px; top:165px;">500g Tomaten</span>
  <span class="box-item box-item--md" style="left:237px; top:188px;">1 Knollensellerie</span>
  <span class="box-item box-item--lg" style="left:356px; top:188px;">1 Salat</span>
  <span class="box-item box-item--lg" style="left:237px; top:211px;">500g Möhren</span>
  <span class="box-item box-item--lg" style="left:347px; top:211px;">1 Spitzkohl</span>
  <span class="box-item box-item--lg" style="left:233px; top:234px;">1 Salatgurke</span>
  <span class="box-item box-item--lg" style="left:336px; top:234px;">500g Zucchini</span>
  <span class="box-item box-item--md" style="left:326px; top:258px;">1 Bund Petersilie</span>
  <span class="box-item box-item--lg" style="left:317px; top:282px;">300g Zwiebeln</span>

  <p class="abs back-text">
    <span class="back-text__line" style="width:210px;">&emsp;Als Gemüsekisten-Abonnent leistest Du</span>
    <span class="back-text__line" style="width:202px;">einen wichtigen Beitrag für die regionale</span>
    <span class="back-text__line" style="width:194px;">Landwirtschaft. Und Du bist sicher, jede</span>
    <span class="back-text__line" style="width:186px;">Woche frisches Gemüse direkt aus</span>
    <span class="back-text__line" style="width:178px;">Musterdorf zu erhalten und zahlst</span>
    <span class="back-text__line back-text__line--end">weniger als beim Kauf am Stand.</span>
  </p>

  <h3 class="abs short-title">&nbsp;&nbsp;&nbsp;Abokiste - kurz und<br>knackig erklärt:</h3>

  <span class="fact" style="left:270px; top:400px;">• Jede Woche 8 bis 10 Gemüse-</span>
  <span class="fact" style="left:259px; top:421px;">sorten sowie Kräuter</span>
  <span class="fact" style="left:254px; top:442px;">• Abo von Mai bis Dezember</span>
  <span class="fact" style="left:246px; top:463px;">• 20€ pro Woche</span>
  <span class="fact" style="left:238px; top:484px;">• Keine chemisch-synthetischen Dünger</span>
  <span class="fact" style="left:227px; top:505px;">oder Spritzmittel</span>
  <span class="fact" style="left:222px; top:526px;">• Abholung in Musterdorf</span>

  <footer class="footer">
    <div class="footer__item" style="left:87px; top:20px;">
      <svg class="icon" width="25" height="25" viewBox="0 0 24 24" aria-hidden="true"><circle cx="12" cy="12" r="12" fill="var(--teal)"/><circle cx="12" cy="9.5" r="3.6" fill="var(--yellow)"/><path d="M5.5 18c1.2-3 3.7-4.3 6.5-4.3s5.3 1.3 6.5 4.3z" fill="var(--yellow)"/></svg>
      <span style="display:block; margin-top:4px;">Jonas Berger (0152 1234 5678)</span>
    </div>
    <span class="footer__rule" style="left:161px; top:17px; height:45px;"></span>
    <div class="footer__item" style="left:235px; top:20px;">
      <svg class="icon" width="25" height="25" viewBox="0 0 24 24" aria-hidden="true"><circle cx="12" cy="12" r="12" fill="var(--teal)"/><rect x="6" y="8" width="12" height="8.5" rx="1" fill="var(--yellow)"/><path d="M6.5 8.5l5.5 4.5 5.5-4.5" fill="none" stroke="var(--teal)" stroke-width="1.2"/></svg>
      <span style="display:block; margin-top:4px;">Feldweg 7, 12345 Musterdorf</span>
    </div>
    <span class="footer__rule" style="left:310px; top:20px; height:42px;"></span>
    <div class="footer__item" style="left:393px; top:21px;">www.gemuesehof-kleineracker-beispiel.de<br>info@gemuesehof-kleineracker-beispiel.de</div>
  </footer>
</section>

</body>
</html>
```